Dog training that every member of the family can use. Humane safe and effective

Starting my own dog training business I would like a pic/drawing of human dog bonding, perhaps a paw in a human hand. Because I deal with all families/people I don't want a specific gender/age to be recognized. Also, to I would like it colorful to stand out since it is a big advertising tool for me. Paw prints included may be a nice feature.

Target Market(s)

People that are looking for a positive reinforcement dog trainer

Industry/Entity Type

Dog Training

Contact Information for Business Card

Vibrantly colored/eye catching business card.
Under Business name: "Helping build an everlasting bond"
Besides business name, Also Include:
place for my name
that I'm Owner/Trainer
email
phone #
web
Services provided:
private lessons
basic pet etiquette
behavior modification

Font styles to use
Other font styles liked:
• Lobster

Requirements
Must have
• paw prints, human hand shaking dogs paw (happy dog/panting)
Nice to have
• colors that attract the eye but not too busy

```html
<!DOCTYPE html>
<html lang="en">
<head>
<meta charset="utf-8">
<title>Kindred Paws – Business Card</title>
<link rel="stylesheet" href="https://fonts.googleapis.com/css2?family=Montserrat:wght@200;300;400;700;800&display=swap">
<style>
  :root {
    --backdrop: #e6e7e9;
    --card-deep: #0f4656;
    --card-mid: #175f72;
    --card-light: #1f7288;
    --band: #2a8fb0;
    --band-text: #d9f1fa;
    --name: #bfeef9;
    --title: #9fc6d2;
    --cream: #f3ead8;
    --accent: #f39a1e;
    --text: #e6f4f8;
    --rule: #8bb7c4;
  }
  * { box-sizing: border-box; margin: 0; padding: 0; }
  html, body {
    width: 1200px; height: 800px; overflow: hidden;
    background: var(--backdrop);
    font-family: "Montserrat", Arial, sans-serif;
  }
  .card {
    position: absolute; left: 100px; top: 114px;
    width: 1000px; height: 572px;
    overflow: hidden;
    box-shadow: 0 10px 30px rgba(0,0,0,0.18);
  }
  .card-texture {
    position: absolute; inset: 0;
    background:
      radial-gradient(ellipse at 75% 40%, var(--card-light) 0%, transparent 60%),
      linear-gradient(150deg, var(--card-deep) 0%, var(--card-mid) 55%, var(--card-deep) 100%);
  }
  .brand {
    position: absolute; left: 70px; top: 270px;
  }
  .brand-mark {
    display: flex; align-items: center; gap: 14px;
  }
  .brand-dot {
    width: 40px; height: 40px; border-radius: 50%;
    background: var(--accent);
  }
  .brand-name {
    font-weight: 400; font-size: 34px; letter-spacing: 2px;
    color: var(--cream); line-height: 1.2;
  }
  .brand-tagline {
    margin-top: 6px;
    font-weight: 300; font-size: 25px;
    color: var(--cream);
  }
  .person {
    position: absolute; right: 70px; top: 110px; text-align: right;
  }
  .person-name {
    font-weight: 800; font-size: 58px; color: var(--name); line-height: 1.05;
  }
  .person-role {
    font-weight: 200; font-size: 42px; color: var(--title); line-height: 1.2;
  }
  .contact {
    position: absolute; right: 70px; top: 320px;
    text-align: right; color: var(--text);
  }
  .contact-rule {
    width: 210px; height: 1px; background: var(--rule);
    margin: 0 0 14px auto;
  }
  .contact-line {
    display: flex; justify-content: flex-end; align-items: center; gap: 12px;
    font-size: 20px; font-weight: 400; line-height: 1.35;
  }
  .contact-line.web { font-weight: 700; font-size: 18px; }
  .contact-icon {
    width: 20px; height: 20px; flex: none;
  }
  .services-band {
    position: absolute; left: 0; right: 0; bottom: 38px; height: 46px;
    background: var(--band);
    display: flex; align-items: center; padding-left: 40px;
    font-size: 21px; font-weight: 400; color: var(--band-text);
  }
</style>
</head>
<body>
  <section class="card" aria-label="Kindred Paws business card">
    <div class="card-texture" role="img" aria-label="Deep teal faceted polygon background"></div>

    <div class="person">
      <h1 class="person-name">Dana Whitfield</h1>
      <p class="person-role">Owner/ Trainer</p>
    </div>

    <div class="brand">
      <div class="brand-mark">
        <span class="brand-dot"></span>
        <span class="brand-name">KINDRED PAWS</span>
      </div>
      <p class="brand-tagline">helping build an everlasting bond</p>
    </div>

    <div class="contact">
      <div class="contact-rule"></div>
      <p class="contact-line">555-014-2290
        <svg class="contact-icon" viewBox="0 0 20 20" aria-hidden="true">
          <circle cx="10" cy="10" r="9" fill="none" stroke="currentColor" stroke-width="1.2"/>
          <path d="M7 5.5l1.6 2.2-1 1.1a6 6 0 0 0 3.6 3.6l1.1-1 2.2 1.6-.9 1.5c-3.8 0-7.6-3.8-7.6-7.6z" fill="currentColor"/>
        </svg>
      </p>
      <p class="contact-line">dana.whitfield@mailbox.net
        <svg class="contact-icon" viewBox="0 0 20 20" aria-hidden="true">
          <circle cx="10" cy="10" r="9" fill="none" stroke="currentColor" stroke-width="1.2"/>
          <rect x="5.5" y="7" width="9" height="6.5" fill="none" stroke="currentColor" stroke-width="1.2"/>
          <path d="M5.5 7l4.5 3.6L14.5 7" fill="none" stroke="currentColor" stroke-width="1.2"/>
        </svg>
      </p>
      <p class="contact-line web">danawhitfield.sitebuilder.com/<br>pawbond
        <svg class="contact-icon" viewBox="0 0 20 20" aria-hidden="true">
          <circle cx="10" cy="10" r="9" fill="none" stroke="currentColor" stroke-width="1.2"/>
          <path d="M5.5 10L10 6l4.5 4M7 9v5h6V9" fill="none" stroke="currentColor" stroke-width="1.2"/>
        </svg>
      </p>
    </div>

    <div class="services-band">Services provided: private lessons - basic pet etiquette - behavior modification</div>
  </section>
</body>
</html>
```